Telepsychology Services

The company is called 'Vantor' and it is a telehealth business.

I would like a lego which has some sort of telecommunications or health feel to it, with the message 'New Technology. New You' incoproated in it.

On the front side of the side I would like the logo with the message 'Providing psychological services to 'hard-to-reach' individuals' printed in large font . I also need the message 'Real-time internet webcam conferencing' located on the front, along with the website address www.vantorclinic.com.au.

On the backside of the card, I would appreicate the following information

Suitable for individuals
•living in remote areas of Australia,
•who experience impairment which leaves them housebound,
•with limited time availability for appointments, and
•for whom high levels of confidentiliaty are important

Designed for individuals with minimal or no webcam experience

Benefits provided by specific private health insurers, ie KELM

All Psychologists registered with the Commonwealth Clinical Practice Licensing Bureau and members with the National Counselling Guild
Updates

Hi All,

Just a quick update.. I think I will prefer logos and busiiness cards that are relatively simple and understated. I am not a big fan of bright, multi colours and fancy designs. Just something clean, crisp, straightforward with a little colour ie blues and greens a good.

Also, for the back page, please keep in simple dot point form...

Thanks,

Mira

Industry/Entity Type

Telecommunications

Contact Information for Business Card

Vantor
www.vantorclinic.com.au

```html
<!DOCTYPE html>
<html lang="en">
<head>
<meta charset="utf-8">
<title>Vantor – Suitable for individuals</title>
<link rel="stylesheet" href="https://fonts.googleapis.com/css2?family=Open+Sans:wght@300&display=swap">
<style>
  :root {
    --page: #ffffff;
    --card: #fbfcfd;
    --teal: #56b2b5;
  }
  html, body {
    margin: 0;
    padding: 0;
    width: 1200px;
    height: 741px;
    overflow: hidden;
    background: var(--page);
  }
  .card-back {
    position: relative;
    width: 1200px;
    height: 741px;
    font-family: 'Open Sans', sans-serif;
    font-weight: 300;
    color: var(--teal);
  }
  .card-panel {
    position: absolute;
    left: 27px;
    top: 38px;
    width: 1146px;
    height: 662px;
    background: var(--card);
  }
  .audience-title {
    position: absolute;
    left: 0;
    width: 1200px;
    top: 152px;
    margin: 0;
    text-align: center;
    font-size: 47px;
    font-weight: 300;
    line-height: 64px;
  }
  .audience-title span {
    display: inline-block;
    padding: 0 10px 0 6px;
    border-bottom: 2px solid var(--teal);
    line-height: 56px;
  }
  .audience-list {
    position: absolute;
    left: 0;
    top: 231px;
    width: 1200px;
    margin: 0;
    padding: 0;
    list-style: none;
    text-align: center;
    font-size: 36px;
    line-height: 47.5px;
    white-space: nowrap;
  }
  .footer-note {
    position: absolute;
    margin: 0;
    text-align: center;
    font-size: 31.3px;
    line-height: 38px;
    white-space: nowrap;
  }
  .insurer-note {
    left: 28px;
    width: 560px;
    top: 558px;
  }
  .registration-note {
    left: 592px;
    width: 560px;
    top: 540px;
  }
  .footer-divider {
    position: absolute;
    left: 590px;
    top: 549px;
    width: 2px;
    height: 93px;
    background: var(--teal);
  }
</style>
</head>
<body>
  <main class="card-back">
    <div class="card-panel"></div>

    <h1 class="audience-title"><span>Suitable for individuals</span></h1>

    <ul class="audience-list">
      <li>{ living in remote areas of Australia }</li>
      <li>{ Housebound or experiencing impairment }</li>
      <li>{ with limited time availability for appointments }</li>
      <li>{ with high levels of confidentiliaty }</li>
      <li>{ with no webcam experience needed }</li>
    </ul>

    <p class="footer-note insurer-note">Benefits provided by specific<br>private health insurers, ie KELM.</p>
    <div class="footer-divider"></div>
    <p class="footer-note registration-note">All Psychologists registered with<br>the Commonwealth Clinical Practice<br>Licensing Bureau</p>
  </main>
</body>
</html>
```